Crestwell Grand Piano Academy is a comprehensive piano studio located in CBD area and provide individual piano lessons.

We also provide services for wedding organising band, or instrumental hiring or venue hiring, or organise concert to students.

I want my name card to be very creative, does not have to be the form or shape with the normal name card, can be in different shape. Also, I want the name card to be very upper class, because learning piano is a serious thing, so I do not want people to bargain with the prices. I want people to see it as a very elegant tuition so that they do not want to bargain and think it is worth to try.

Further more, Crestwell Grand Piano Academy is not like normal piano studio only provide piano lessons, we provide band services for each other event, such as cruise party, wedding etc. I want people to see it as owner of Grand Piano Academy, they will have different type of services all in one, I provide more than that, and I am well connected. I do not provide only piano lesson, but also all other musical knowledge and I am very professional

I want name card to be very simple, just name of company name, my name and website that's all, maybe phone number and email as well.

Please check my website to have more ideal concept.
http://dorvanpeq.sitebuild.example/crestwellpianoacademy

Target Market(s)

For all people who love to play piano (better with upper class)

Industry/Entity Type

Wedding

Contact Information for Business Card

Clara Voss
Mobile:0419876502
Email: crestwellgrandstudio@mailbrook.example

Colors

Designer to choose colors to be used in the design.

Requirements
Must have
• Creativity
Nice to have
• Black and white
some sort of piano image
Should not have
• Childish

```html
<!DOCTYPE html>
<html lang="en">
<head>
<meta charset="utf-8">
<title>Crestwell Grand Piano Academy — Business Card</title>
<link href="https://fonts.googleapis.com/css2?family=Source+Sans+3:wght@400;700&display=swap" rel="stylesheet">
<style>
  :root {
    --page-bg: #ffffff;
    --card-black: #000000;
    --ink-white: #ffffff;
    --rail-grey: #3c3c3c;
    --clef-grey: #3a3a3a;
    --key-light: #ffffff;
    --key-shade: #9a9a9a;
  }
  html, body {
    margin: 0;
    padding: 0;
    overflow: hidden;
    background: var(--page-bg);
  }
  .canvas {
    position: relative;
    width: 1200px;
    height: 1000px;
    overflow: hidden;
    background: var(--page-bg);
    font-family: "Source Sans 3", "Myriad Pro", Arial, sans-serif;
    color: var(--ink-white);
  }
  .card-shapes {
    position: absolute;
    inset: 0;
  }
  .card-text {
    position: absolute;
    margin: 0;
    white-space: nowrap;
    line-height: 1;
  }
  .front-name {
    left: 622px;
    top: 185px;
    transform: translateX(-50%);
    font-size: 32px;
    font-weight: 700;
  }
  .front-company {
    left: 628px;
    top: 240px;
    transform: translateX(-50%);
    font-size: 32px;
    font-weight: 400;
  }
  .back-name {
    left: 481px;
    top: 729px;
    font-size: 32px;
    font-weight: 700;
  }
  .contact-list {
    position: absolute;
    left: 525px;
    top: 815px;
    margin: 0;
    padding: 0;
    list-style: none;
  }
  .contact-item {
    height: 42px;
    font-size: 19px;
    line-height: 20px;
    white-space: nowrap;
  }
  .contact-item--web {
    font-size: 16px;
  }
</style>
</head>
<body>
<main class="canvas">
  <svg class="card-shapes" width="1200" height="1000" viewBox="0 0 1200 1000" xmlns="http://www.w3.org/2000/svg">
    <defs>
      <clipPath id="front-card-clip">
        <path d="M222,47 H915 Q960,47 960,92 V310 Q960,355 915,355 H758 Q702,355 702,411 V425 Q702,462 665,462 H225 Q200,462 200,437 V69 Q200,47 222,47 Z"/>
      </clipPath>
      <linearGradient id="keyboard-tone" x1="0" y1="0" x2="1" y2="0">
        <stop offset="0" stop-color="var(--key-light)"/>
        <stop offset="0.45" stop-color="#e6e6e6"/>
        <stop offset="1" stop-color="var(--key-shade)"/>
      </linearGradient>
    </defs>

    <!-- Front card -->
    <g class="front-card" clip-path="url(#front-card-clip)">
      <rect x="200" y="47" width="760" height="415" fill="var(--card-black)"/>
      <rect class="keyboard-area" x="200" y="47" width="136" height="415" fill="url(#keyboard-tone)" role="img" aria-label="Piano keyboard seen from above, white and black keys"/>
      <rect class="rail-line" x="370" y="47" width="8" height="415" fill="var(--rail-grey)"/>
    </g>

    <!-- Back card -->
    <g class="back-card">
      <path d="M245,538 H915 Q960,538 960,583 V910 Q960,950 920,950 H500 Q460,950 460,910 V900 Q460,845 405,845 H245 Q200,845 200,800 V583 Q200,538 245,538 Z" fill="var(--card-black)"/>
      <rect class="clef-area" x="272" y="548" width="108" height="288" rx="48" fill="var(--clef-grey)" role="img" aria-label="Large treble clef decoration in dark grey"/>

      <!-- contact icons -->
      <g class="icon-phone" fill="none" stroke="var(--ink-white)" stroke-width="2">
        <rect x="484" y="814" width="14" height="24" rx="2"/>
        <line x1="484" y1="818" x2="498" y2="818"/>
        <line x1="484" y1="833" x2="498" y2="833"/>
      </g>
      <g class="icon-mail" fill="none" stroke="var(--ink-white)" stroke-width="2">
        <rect x="481" y="861" width="21" height="15"/>
        <polyline points="481,861 491.5,870 502,861"/>
        <line x1="481" y1="876" x2="488" y2="869"/>
        <line x1="502" y1="876" x2="495" y2="869"/>
      </g>
      <g class="icon-web" fill="none" stroke="var(--ink-white)" stroke-width="1.8">
        <circle cx="491.5" cy="909" r="9.5"/>
        <ellipse cx="491.5" cy="909" rx="4.2" ry="9.5"/>
        <line x1="482" y1="909" x2="501" y2="909"/>
        <line x1="484" y1="904" x2="499" y2="904"/>
        <line x1="484" y1="914" x2="499" y2="914"/>
      </g>
      <rect class="contact-divider" x="512" y="815" width="3" height="105" fill="var(--ink-white)"/>
    </g>
  </svg>

  <p class="card-text front-name">CLARA VOSS</p>
  <p class="card-text front-company">CRESTWELL GRAND PIANO ACADEMY</p>

  <p class="card-text back-name">CLARA VOSS</p>
  <ul class="contact-list">
    <li class="contact-item">0419876502</li>
    <li class="contact-item">crestwellgrandstudio@mailbrook.example</li>
    <li class="contact-item contact-item--web">http://dorvanpeq.sitebuild.example/crestwellpianoacademy</li>
  </ul>
</main>
</body>
</html>
```